Clean Modern Skin Product branding/ label.

I need a label for a skincare line. The company is Velmora but product names will vary. A couple products to list are:
Sensitive Cleanser, Tevola, Ostiva, Malo ve, Quintel, Quintel Plus, Quintel Intense, Dovira, Ambrel and Fenwyn.

I would like the color scheme to be muted greens, grays, tourquise. The bottles are white, boston shaped with pumps, and ounces are 2, 4, 8, 16 ounces. When I choose the design, I can give you exact label sizes. Along with the ingredience already on the product label.

The look I desire is clean, minimal. A modern, organic look. Ideas that come to mind are a Ostrelle,https://www.ostrelle-beauty.example/product/1573/15501/3-step/step-2-exfoliate/clarifying-lotion-1 and the simplicity of Vo Tenn.

Both styles high light the name, in this case Velmora, and then the specific product.

My product is clean utilizing pure ingredients rather that a bunch fillers and binders. When I work with my clients I normally will say we need to "restore the balance" from over use of harsh products. That is why this lines works. It restores the skin to it's natural state. The process is simple, so I would like the label to reflect that simplicity.

Target Market(s)

Anyone with sensitive skin. So gender neutral

Industry/Entity Type

Skin Care Product

Font styles to use
Serif
Sans Serif
Decorative

Colors
acd037
33b8a4
fcfefd
85cae6
d3d3d3

Requirements
Must have
• Logo, name of product and color identity for cleanser, Active products, moisturizers
• I am thinking we could have one color for a cleanser and a space where I can put a sticker on which cleanser it is. Acne Cleasner, Sensitive Cleanser, and Cleanser.
Nice to have
• Not sure....suprise me. I would like the font to stay the same on the VELMORA, but you can change color, or color of leaf.
Should not have
• Too busy, too crowded or look like every other skincare line

```html
<!DOCTYPE html>
<html lang="en">
<head>
<meta charset="UTF-8">
<title>Velmora — Quintel Plus Label</title>
<link href="https://fonts.googleapis.com/css2?family=League+Spartan:wght@400;500;700&family=Josefin+Sans:wght@300;400&family=Tinos&display=swap" rel="stylesheet">
<style>
  :root {
    --lavender: #d9d3ea;
    --lavender-deep: #cbc4e4;
    --sky: #a9c9ee;
    --sky-soft: #bdd6f2;
    --pearl: #ebe6f4;
    --ink-white: #ffffff;
  }
  html, body {
    margin: 0;
    padding: 0;
    overflow: hidden;
  }
  body {
    width: 914px;
    height: 1200px;
    background: var(--lavender);
  }
  .label {
    position: relative;
    width: 914px;
    height: 1200px;
    overflow: hidden;
    color: var(--ink-white);
  }
  .label__marble {
    position: absolute;
    inset: 0;
    background:
      radial-gradient(ellipse 380px 260px at 80% 8%, var(--sky-soft) 0%, transparent 70%),
      radial-gradient(ellipse 420px 320px at 18% 30%, var(--sky) 0%, transparent 72%),
      radial-gradient(ellipse 360px 300px at 88% 52%, var(--sky) 0%, transparent 70%),
      radial-gradient(ellipse 460px 300px at 30% 78%, var(--sky-soft) 0%, transparent 70%),
      radial-gradient(ellipse 300px 220px at 60% 96%, var(--pearl) 0%, transparent 70%),
      linear-gradient(160deg, var(--lavender) 0%, var(--lavender-deep) 45%, var(--lavender) 100%);
  }
  .label__brand {
    position: absolute;
    left: 252px;
    top: 172px;
    margin: 0;
    font-family: "League Spartan", sans-serif;
    font-weight: 500;
    font-size: 68px;
    letter-spacing: 1px;
    line-height: 1;
  }
  .label__product {
    position: absolute;
    left: 252px;
    top: 318px;
    margin: 0;
    font-family: "League Spartan", sans-serif;
    font-weight: 700;
    font-size: 80px;
    line-height: 88px;
    letter-spacing: -0.5px;
  }
  .label__tagline {
    position: absolute;
    left: 252px;
    top: 556px;
    margin: 0;
    font-family: "Josefin Sans", sans-serif;
    font-weight: 400;
    font-size: 25px;
    letter-spacing: 0.5px;
  }
  .label__description {
    position: absolute;
    left: 252px;
    top: 598px;
    width: 486px;
    margin: 0;
    font-family: "Tinos", serif;
    font-size: 27px;
    line-height: 35.5px;
  }
  .label__volume {
    position: absolute;
    left: 252px;
    top: 968px;
    margin: 0;
    font-family: "League Spartan", sans-serif;
    font-weight: 700;
    font-size: 26px;
    letter-spacing: 0.3px;
  }
</style>
</head>
<body>
  <main class="label">
    <div class="label__marble" role="img" aria-label="Soft swirling lavender and sky-blue marbled liquid background"></div>
    <p class="label__brand">velmora</p>
    <h1 class="label__product">Quintel<br>Plus.</h1>
    <h2 class="label__tagline">RESTORE THE BALANCE</h2>
    <p class="label__description">Lilutpat ut wisi eniml orem ipsum dolor sit amet, consectetuer adipiscing elit, sed diam nonummy nibh euismod tincidunt ut laoreet dolore magna aliquam erat volutpat. Ut wisi enim ad minim veniam, quis nostrud exerci tation ullamcorper suscipit lobortis nisl ut aliquip ex ea commodo consequat.</p>
    <p class="label__volume">16FL.OZ — 500ML</p>
  </main>
</body>
</html>
```